Creative Stationary for Solo Law Firm

I am looking for stationary designs for my solo law firm called TM Halvorsen Law PLLC. My logo is attached. I'd like the logo incorporated into the design.

I'm looking for a stationary design that is a bit outside of the box and not too standard or boring. The final design should communicate professionalism.

Target Market(s)

United States Clients, Opposing Counsel

Industry/Entity Type

Legal

Font styles to use
Sans Serif

Requirements
Must have
• The stationary design must incorporate my logo design attached. The design itself must be creative. The envelope design must follow standard United States designs with room for the postage stamp at the top right corner and space for the recipient's address in the middle.

```html
<!DOCTYPE html>
<html lang="en">
<head>
<meta charset="utf-8">
<title>TM Halvorsen Law PLLC – Business Cards</title>
<link rel="stylesheet" href="https://fonts.googleapis.com/css2?family=Cinzel:wght@500&family=Arimo:wght@400;700&display=swap">
<style>
  :root {
    --navy: #1a2f6e;
    --navy-deep: #10205a;
    --navy-light: #2a4391;
    --silver: #b3b5ba;
    --silver-light: #d9dadd;
    --paper: #ffffff;
    --backdrop: #eceae6;
    --ink-light: #f3f5fb;
  }
  * { margin: 0; padding: 0; box-sizing: border-box; }
  html, body {
    width: 1200px; height: 950px; overflow: hidden;
    background: var(--backdrop);
  }
  .sheet {
    position: relative; width: 1200px; height: 950px;
    display: flex; flex-direction: column; align-items: center; justify-content: center; gap: 44px;
  }
  .card {
    position: relative; width: 720px; height: 411px; overflow: hidden;
    box-shadow: 0 8px 24px rgba(0,0,0,0.18);
  }

  /* Back of card */
  .card--back {
    background: linear-gradient(120deg, var(--navy-deep) 0%, var(--navy) 55%, var(--navy-light) 100%);
    display: flex; flex-direction: column; align-items: center; justify-content: center; gap: 28px;
  }
  .back-name {
    font-family: "Cinzel", serif; font-weight: 500;
    font-size: 46px; letter-spacing: 1px; color: var(--silver);
  }
  .back-web {
    font-family: "Arimo", sans-serif; font-size: 20px; letter-spacing: 1px; color: var(--silver);
  }

  /* Front of card */
  .card--front { background: var(--paper); }
  .card-wave { position: absolute; inset: 0; width: 720px; height: 411px; }
  .firm-name {
    position: absolute; left: 64px; top: 62px;
    font-family: "Cinzel", serif; font-weight: 500;
    font-size: 33px; color: var(--navy); letter-spacing: 0.5px;
  }
  .contact {
    position: absolute; right: 34px; top: 200px;
    text-align: right; color: var(--ink-light);
    font-family: "Arimo", sans-serif;
  }
  .contact-name { font-weight: 700; font-size: 22px; line-height: 25px; letter-spacing: 0.5px; }
  .contact-role { font-size: 17px; line-height: 20px; margin-bottom: 8px; }
  .contact-line { font-size: 17px; line-height: 22px; }
  .contact-row {
    display: flex; justify-content: flex-end; align-items: center; gap: 8px;
    font-size: 17px; line-height: 22px;
  }
  .contact-row svg { width: 16px; height: 16px; fill: var(--ink-light); flex: none; }
  .address { margin-bottom: 4px; }
</style>
</head>
<body>
<main class="sheet">

  <section class="card card--back" aria-label="Card back">
    <div class="back-name">TM Halvorsen Law</div>
    <div class="back-web">www.tmhalvorsen.com</div>
  </section>

  <section class="card card--front" aria-label="Card front">
    <svg class="card-wave" viewBox="0 0 720 411" aria-hidden="true">
      <defs>
        <linearGradient id="navyFill" x1="0" y1="0" x2="1" y2="1">
          <stop offset="0" stop-color="#2a4391"/>
          <stop offset="0.6" stop-color="#1a2f6e"/>
          <stop offset="1" stop-color="#10205a"/>
        </linearGradient>
        <linearGradient id="silverFill" x1="0" y1="0" x2="1" y2="0">
          <stop offset="0" stop-color="#9fa1a6"/>
          <stop offset="0.5" stop-color="#c6c8cc"/>
          <stop offset="1" stop-color="#e2e3e5"/>
        </linearGradient>
      </defs>
      <path fill="url(#silverFill)"
        d="M0,200 C150,300 330,290 470,200 C560,142 640,120 720,118 L720,128 C640,135 560,160 470,220 C330,320 150,328 0,232 Z"/>
      <path fill="url(#navyFill)"
        d="M0,232 C150,328 330,320 470,220 C560,160 640,135 720,128 L720,411 L0,411 Z"/>
    </svg>

    <h1 class="firm-name">TM Halvorsen Law</h1>

    <div class="contact">
      <div class="contact-name">DANIEL MARSH</div>
      <div class="contact-role">President</div>
      <div class="address">
        <div class="contact-line">2719 Linden Court</div>
        <div class="contact-line">Riverside, NY 11020</div>
      </div>
      <div class="contact-row">555 0142 7781
        <svg viewBox="0 0 16 16"><path d="M3 2h3l1.5 3.5-2 1.3a8 8 0 0 0 3.7 3.7l1.3-2L14 10v3a1 1 0 0 1-1 1A11 11 0 0 1 2 3a1 1 0 0 1 1-1z"/></svg>
      </div>
      <div class="contact-row">555 0198 3346
        <svg viewBox="0 0 16 16"><path d="M5 1h6a1 1 0 0 1 1 1v12a1 1 0 0 1-1 1H5a1 1 0 0 1-1-1V2a1 1 0 0 1 1-1zm0 2v9h6V3zm3 10a.8.8 0 1 0 0 1.6A.8.8 0 0 0 8 13z"/></svg>
      </div>
      <div class="contact-row">dmarsh@tmhalvorsen.com
        <svg viewBox="0 0 16 16"><path d="M1 4h14v9H1zm1 1v.4l6 4 6-4V5zm0 1.6V12h12V6.6l-6 4z"/></svg>
      </div>
      <div class="contact-row">www.tmhalvorsen.com
        <svg viewBox="0 0 16 16"><path d="M8 1a7 7 0 1 0 0 14A7 7 0 0 0 8 1zm0 1.5c.8 0 1.7 1.5 2 3.5H6c.3-2 1.2-3.5 2-3.5zM2.6 7h2.9a12 12 0 0 0 0 2H2.6a5.5 5.5 0 0 1 0-2zm3.9 0h3a11 11 0 0 1 0 2h-3a11 11 0 0 1 0-2zm4 0h2.9a5.5 5.5 0 0 1 0 2h-2.9a12 12 0 0 0 0-2zM6 10h4c-.3 2-1.2 3.5-2 3.5S6.3 12 6 10z"/></svg>
      </div>
    </div>
  </section>

</main>
</body>
</html>
```